Skin Care Company Branding/Design for Product Packaging

Hello,

We need help with designing box/container graphics for our skin care company, Velvora Beauty Co.

I've attached two boxes from our competitors. One is a pimple patch box and one is a dry face towel box.

We want our brand to appear professional, modern, and clean.

We want the design and colors for all of our products to go together.

Please do your design work on the images we provided. You can remove any content from the other brands. If you have major issues with these images please use something very similar.

The product details our products and our competitors will be almost identical but our company name and the colors will be different.

Please take your time on this. We have already done several products on this page and will have many more to come. If we really like your work we could select you to work with us.

The box dimensions for the face towels are: 6.25 x 5.25 x 4.75. If you are having trouble seeing the image please use the Dewmoss Face Lab 50 count image off of Trovamart.

The box dimensions or the acne patches are: 5.5 x 3.25 x 0.75. If you are having trouble seeing the image please us the Nimbo Quell Dot (red and white box) on Trovamart.

Our boxes for these two products are a carton type paper.

We are open to colors but it needs to look very clean, modern and eye catching. We are open to any color combination but particularly like the idea of an color combination of white and another color like Dulmira or the Nimbo Quell Dot box.

Target Market(s)

Towels will be primarily female. Acne patches will be both male and female but primarily female.

Industry/Entity Type

Health & Beauty Products

Requirements
Must have
• Design work on the boxes in the images I provided.

```html
<!DOCTYPE html>
<html lang="en">
<head>
<meta charset="utf-8">
<title>Velvora Beauty Co. — Acne Patch Box Front</title>
<link rel="stylesheet" href="https://fonts.googleapis.com/css2?family=Fira+Sans:ital,wght@0,400;0,500;0,700;1,700&display=swap">
<style>
  :root {
    --page-bg: #ffffff;
    --panel-bg: #ffffff;
    --panel-edge: #ececec;
    --blush: #f2d5e5;
    --magenta: #e8197a;
    --magenta-soft: #f3c4dc;
    --orchid: #e9a8cf;
    --ink: #111111;
    --ink-soft: #2a2a2a;
    --patch-light: #ece2c6;
    --patch-dark: #c9b98f;
    --logo-ink: #d98bb6;
    --hole-edge: #d9d9d9;
  }
  * { margin: 0; padding: 0; box-sizing: border-box; }
  html, body {
    width: 1200px; height: 1200px; overflow: hidden;
    background: var(--page-bg);
    font-family: "Fira Sans", Arial, sans-serif;
  }
  .canvas { position: relative; width: 1200px; height: 1200px; }

  .box-front {
    position: absolute; left: 340px; top: 165px;
    width: 520px; height: 875px;
    background: var(--panel-bg);
    box-shadow: 0 0 0 1px var(--panel-edge);
    overflow: hidden;
  }
  .box-shapes { position: absolute; inset: 0; }

  .brand-name {
    position: absolute; left: 24px; top: 27px;
    font-weight: 500; font-size: 18px; letter-spacing: 0.5px;
    color: var(--logo-ink);
    white-space: nowrap;
  }

  .title-line {
    position: absolute; left: 48px;
    font-weight: 700; font-style: italic;
    font-size: 104px; line-height: 1; letter-spacing: 3px;
    color: var(--magenta);
  }
  .title-acne { top: 471px; }
  .title-patch { top: 586px; }

  .variant {
    position: absolute; left: 42px; top: 700px;
    font-weight: 700; font-style: italic; font-size: 30px;
    letter-spacing: 0.5px;
    color: var(--orchid);
  }

  .count {
    position: absolute; left: 70px; top: 772px;
    width: 60px; text-align: center; color: var(--ink);
  }
  .count-number { display: block; font-weight: 700; font-size: 50px; line-height: 48px; }
  .count-unit { display: block; font-weight: 700; font-size: 18px; line-height: 20px; }

  .count-divider {
    position: absolute; left: 131px; top: 774px;
    width: 2px; height: 62px; background: var(--ink);
  }

  .claims {
    position: absolute; left: 147px; top: 772px;
    font-size: 15px; line-height: 22px; color: var(--ink-soft);
  }
</style>
</head>
<body>
<main class="canvas">
  <section class="box-front" aria-label="Acne patch box front panel">
    <svg class="box-shapes" width="520" height="875" viewBox="0 0 520 875">
      <defs>
        <radialGradient id="patchTone" cx="40%" cy="35%" r="70%">
          <stop offset="0%" stop-color="var(--patch-light)"/>
          <stop offset="100%" stop-color="var(--patch-dark)"/>
        </radialGradient>
      </defs>
      <circle class="blush-disc" cx="130" cy="236" r="245" fill="var(--blush)"/>
      <circle class="hang-hole" cx="259" cy="55" r="26" fill="#ffffff" stroke="var(--hole-edge)" stroke-width="1.5"/>
      <rect class="highlight-acne" x="40" y="538" width="260" height="37" fill="var(--magenta-soft)"/>
      <rect class="highlight-patch" x="40" y="653" width="288" height="39" fill="var(--magenta-soft)"/>
      <circle class="patch-visual" role="img" aria-label="Illustration of a round skin-tone acne patch with a peeling corner"
              cx="350" cy="335" r="82" fill="url(#patchTone)"/>
    </svg>

    <div class="brand-name">Velvora Beauty Co.</div>

    <h1 class="title">
      <span class="title-line title-acne">Acne</span>
      <span class="title-line title-patch">Patch</span>
    </h1>
    <p class="variant">Original</p>

    <div class="count">
      <span class="count-number">20</span>
      <span class="count-unit">PCS</span>
    </div>
    <div class="count-divider"></div>
    <p class="claims">
      The pimple emergency patch. Gently<br>
      absorb pimple gunk in 6 - 8 hours.<br>
      Drug-free &amp; dermatologist-reviewed
    </p>
  </section>
</main>
</body>
</html>
```